Harbor Lanterns: Walking Beside Young Ones Through Every Season

This book is about being a good father and how to parent them well so they are fully equipped to launch into the world when they become adults. It is an encouraging and practical guide that acknowledges the difficulties of being a good father and provides strategies for addressing them.

Target Market(s)

My target market is dads, or people that will gift this book to a dad that they know

```html
<!DOCTYPE html>
<html lang="en">
<head>
<meta charset="utf-8">
<title>Harbor Lanterns – Book Cover</title>
<link href="https://fonts.googleapis.com/css2?family=Poppins:wght@400;500&family=Kaushan+Script&display=swap" rel="stylesheet">
<style>
  :root {
    --backdrop: #9a9a9a;
    --paper: #fdfdfd;
    --teal: #18a6cc;
    --navy: #0d3178;
    --wash-sky: #5cc3ea;
    --wash-blue: #2f7fc4;
    --wash-violet: #9a6fb8;
    --wash-rose: #e3a3b8;
  }
  * { margin: 0; padding: 0; box-sizing: border-box; }
  html, body {
    width: 1200px;
    height: 1200px;
    overflow: hidden;
    background: var(--backdrop);
  }
  .cover {
    position: absolute;
    left: 193px;
    top: 0;
    width: 774px;
    height: 1200px;
    background: var(--paper);
    text-align: center;
  }
  .title-kicker {
    position: absolute;
    top: 70px;
    left: 0;
    width: 100%;
    font-family: "Poppins", sans-serif;
    font-weight: 500;
    font-size: 68px;
    letter-spacing: 3px;
    color: var(--teal);
    line-height: 1;
  }
  .title-script {
    position: absolute;
    top: 160px;
    left: 0;
    width: 100%;
    font-family: "Kaushan Script", cursive;
    font-size: 150px;
    color: var(--navy);
    line-height: 1.1;
    transform: rotate(-3deg);
  }
  .subtitle {
    position: absolute;
    top: 322px;
    left: 0;
    width: 100%;
    font-family: "Poppins", sans-serif;
    font-weight: 400;
    font-size: 27px;
    line-height: 35px;
    letter-spacing: 0.5px;
    color: var(--navy);
    text-transform: uppercase;
  }
  .cover-art {
    position: absolute;
    left: 101px;
    top: 432px;
    width: 570px;
    height: 714px;
    border-radius: 46% 54% 40% 60% / 38% 42% 58% 62%;
    background:
      radial-gradient(ellipse at 60% 25%, rgba(253,253,253,0.95) 0%, rgba(253,253,253,0) 45%),
      radial-gradient(ellipse at 30% 55%, var(--wash-rose) 0%, rgba(227,163,184,0) 40%),
      linear-gradient(170deg, var(--wash-sky) 0%, var(--wash-blue) 50%, var(--wash-violet) 80%, rgba(253,253,253,0) 100%);
    opacity: 0.85;
    filter: blur(6px);
  }
</style>
</head>
<body>
  <main class="cover">
    <h1 class="title">
      <span class="title-kicker">HARBOR</span>
      <span class="title-script">Lanterns</span>
    </h1>
    <p class="subtitle">Walking beside young ones<br>through every season</p>
    <div class="cover-art" role="img" aria-label="Watercolour illustration of a smiling father holding his young daughter, set in splashes of blue, violet and pink"></div>
  </main>
</body>
</html>
```